TKA Electricial Contracting Services

Hi guys, after a design for my small electrical company, have logo design files to be incorporated into the layout, the basic concept is electrical contracting services for residential, commercial, industrial & data services, image is clean clear and strong,

Card format is to have a nice clean logo on front,with maybe the Residential – commercial – industrial - data, followed with licensed & insured, followed by contact details on backside of the card.

Target Market(s)

Residential, commercial, industrial sectors.

Industry/Entity Type

Electrical

Contact Information for Business Card

TKA logo,
Residential – commercial – industrial - data
REC: 61372
Email: tka@poralink.net.au
Phone: 0458 203 719

Requirements
Must have
• Clean & strong design.
Nice to have
• If possible, I would like the logo colours inverted so the text is orange and the background is black on the front of the card, then the backside of the card be the reverse colour
Should not have
• No Sparks, lightning bolts,

```html
<!DOCTYPE html>
<html lang="en">
<head>
<meta charset="utf-8">
<title>TKA Electrical – Business Card</title>
<link href="https://fonts.googleapis.com/css2?family=Exo+2:wght@700&family=Open+Sans:wght@400&display=swap" rel="stylesheet">
<style>
  :root {
    --orange: #f4842f;
    --black: #000000;
    --white: #ffffff;
    --divider: #7a4a22;
  }
  * { margin: 0; padding: 0; box-sizing: border-box; }
  html, body {
    width: 1200px; height: 1000px; overflow: hidden;
    background: var(--white);
  }
  .canvas { position: relative; width: 1200px; height: 1000px; }

  .card { position: absolute; overflow: hidden; }

  /* Front */
  .card-front {
    left: 322px; top: 147px; width: 546px; height: 353px;
    background: var(--black);
  }
  .front-name {
    position: absolute; right: 76px; top: 58px;
    font-family: "Exo 2", sans-serif; font-weight: 700;
    font-size: 182px; line-height: 1; letter-spacing: -4px;
    color: var(--orange);
  }
  .front-tagline {
    position: absolute; right: 76px; top: 228px;
    font-family: "Exo 2", sans-serif; font-weight: 700;
    font-size: 29px; line-height: 1; letter-spacing: 0.5px;
    color: var(--orange);
  }

  /* Back */
  .card-back {
    left: 324px; top: 510px; width: 545px; height: 352px;
    background: var(--orange);
  }
  .back-brand {
    position: absolute; left: 28px; top: 130px; width: 176px;
    text-align: right; font-family: "Exo 2", sans-serif; font-weight: 700;
    color: var(--black);
  }
  .back-brand .brand-name {
    font-size: 76px; line-height: 0.9; letter-spacing: -2px; display: block;
  }
  .back-brand .brand-tagline {
    font-size: 13.5px; line-height: 1.1; display: block; margin-top: 4px;
  }
  .back-brand .brand-licence {
    font-family: "Open Sans", sans-serif; font-weight: 400;
    font-size: 7.5px; display: block; letter-spacing: 0.3px;
  }
  .divider {
    position: absolute; left: 224px; top: 88px; height: 156px;
    border-left: 1.5px dashed var(--divider);
  }
  .contact-list { position: absolute; left: 250px; top: 86px; list-style: none; }
  .contact-item {
    display: flex; align-items: center; height: 57px;
    font-family: "Open Sans", sans-serif; font-size: 20px; color: var(--black);
  }
  .contact-icon { width: 62px; height: 44px; margin-right: 14px; flex: none; }

  .skyline {
    position: absolute; left: 20px; top: 280px; width: 210px; height: 46px;
    background: linear-gradient(to top, #1a1a1a 0%, rgba(26,26,26,0.55) 60%, rgba(26,26,26,0) 100%);
  }
  .ground-band {
    position: absolute; left: 0; bottom: 0; width: 100%; height: 26px;
    background: var(--black);
  }
</style>
</head>
<body>
<div class="canvas">

  <section class="card card-front">
    <div class="front-name">TKA</div>
    <div class="front-tagline">Tyler Kane Electrical</div>
  </section>

  <section class="card card-back">
    <div class="back-brand">
      <span class="brand-name">TKA</span>
      <span class="brand-tagline">Tyler Kane Electrical</span>
      <span class="brand-licence">REC: 61372</span>
    </div>

    <div class="divider"></div>

    <ul class="contact-list">
      <li class="contact-item">
        <svg class="contact-icon" viewBox="0 0 62 44" aria-hidden="true">
          <circle cx="26" cy="22" r="19" fill="none" stroke="#000" stroke-width="5"/>
          <rect x="23" y="0" width="6" height="6" fill="#000"/>
          <rect x="23" y="38" width="6" height="6" fill="#000"/>
          <rect x="5" y="19" width="6" height="6" fill="#000"/>
          <text x="26" y="29" text-anchor="middle" font-family="Exo 2, sans-serif" font-weight="700" font-size="19" fill="#000">24</text>
        </svg>
        <span>Maintenance Service</span>
      </li>
      <li class="contact-item">
        <svg class="contact-icon" viewBox="0 0 62 44" aria-hidden="true">
          <path d="M5 14 Q30 0 55 14 L52 20 L42 18 L41 13 Q30 10 19 13 L18 18 L8 20 Z" fill="#000"/>
          <path d="M14 40 L18 22 L42 22 L46 40 Z" fill="#000"/>
          <g fill="#f4842f">
            <rect x="24" y="25" width="3" height="3"/><rect x="29" y="25" width="3" height="3"/><rect x="34" y="25" width="3" height="3"/>
            <rect x="24" y="30" width="3" height="3"/><rect x="29" y="30" width="3" height="3"/><rect x="34" y="30" width="3" height="3"/>
            <rect x="24" y="35" width="3" height="3"/><rect x="29" y="35" width="3" height="3"/><rect x="34" y="35" width="3" height="3"/>
          </g>
        </svg>
        <span>0458 203 719</span>
      </li>
      <li class="contact-item">
        <svg class="contact-icon" viewBox="0 0 62 44" aria-hidden="true">
          <rect x="1" y="6" width="58" height="34" fill="#000"/>
          <path d="M3 8 L30 27 L57 8" fill="none" stroke="#f4842f" stroke-width="2"/>
        </svg>
        <span>tka@poralink.net.au</span>
      </li>
    </ul>

    <div class="skyline" role="img" aria-label="Silhouette of city buildings, houses and trees along the bottom edge"></div>
    <div class="ground-band"></div>
  </section>

</div>
</body>
</html>
```